Family Medicine Clinic Needs Mailchimp Newsletter Template

Looking for a responsive mailchimp template that matches the theme and overall look/feel of our website brightpathhc.com.

I'm looking for a professional, clean, simple, minimalist, bold design.
Colors would ideally be greens and blues, cool tones, muted colors, or graytones.

See attached word document for content for the upcoming newsletter

Can see prior newsletter content here:
http://brightpathhc.com/ourresources/newsletter-archive/

I have attached a copy of our brochure to see a sample of what we offer

The desired newsletter title would be:
The Bright Path
Looking for a great banner for that

Looking for basically 1 main photo area per text area for future templates

Under September is Comfort Outreach Month want links to our different services I mention

Under the videos section would like a video gallery of sorts that have links to the videos

Lumaderm image ad needs to be redone

Would like a button to take to schedule an appointment and patient portal
Easily visible phone number
Would like to have several sections with buttons to find out more

Would like feedback question at bottom
Rated 7-10 would forward to
https://zipqa.lnk/Rb8kWe

1-6 would send email to us

Reason: I have now guaranteed payment so I am giving a few more days for those designers that still want to submit a design

```html
<!DOCTYPE html>
<html lang="en">
<head>
<meta charset="utf-8">
<title>The Bright Path – September Newsletter</title>
<link href="https://fonts.googleapis.com/css2?family=Roboto:wght@300;400;500;700;900&display=swap" rel="stylesheet">
<style>
:root{
  --page:#f0f0f0;
  --paper:#ffffff;
  --ink:#555a5e;
  --ink-soft:#777c80;
  --ink-strong:#444a4e;
  --accent-orange:#ef8450;
  --rule-dark:#3e6b78;
  --sky:#e2f2fa;
  --brand:#2f7fa6;
  --blue:#3aa2d0;
  --green:#6cb33f;
  --green-soft:#d8e6b8;
  --panel:#f3f3f3;
  --cream:#fbfcf2;
  --yellow:#fde619;
  --dot:#c9c9c9;
}
*{box-sizing:border-box;margin:0;padding:0}
html,body{width:768px;height:1200px;overflow:hidden}
body{background:var(--page);font-family:"Roboto",Arial,sans-serif;color:var(--ink);position:relative}
.abs{position:absolute}
.view-online{left:0;width:768px;top:46px;text-align:center;color:var(--accent-orange);font-size:12px;font-weight:500}
.view-online svg{vertical-align:-3px;margin-right:5px}
.sheet{left:124px;top:76px;width:521px;height:1124px;background:var(--paper)}
.masthead{left:124px;top:76px;width:521px;height:88px;background:var(--sky);border-top:3px solid var(--rule-dark)}
.brand{left:0;width:521px;top:14px;display:flex;justify-content:center;align-items:center;gap:10px;color:var(--brand);font-weight:700}
.brand .mark{width:20px;height:20px;border-radius:50%;background:var(--green)}
.brand .name{font-size:28px;line-height:32px;letter-spacing:.3px}
.brand .sub{display:block;font-size:10px;line-height:16px;letter-spacing:5px;text-align:center}
.issue-title{left:157px;top:186px;color:var(--blue);font-size:19px;font-weight:500}
.issue-list{left:157px;top:216px;list-style:none}
.issue-list li{font-size:10.5px;font-weight:500;color:var(--ink-soft);height:20.8px;padding-left:14px;position:relative}
.issue-list li::before{content:"";position:absolute;left:0;top:4px;width:6px;height:6px;border-radius:50%;background:var(--dot)}
.side-box{left:414px;top:187px;width:197px;height:240px;background:var(--cream);border:1px solid #e2e6d8}
.promo{left:25px;top:13px;width:150px;height:150px;border:2px solid #ddd;background:linear-gradient(160deg,#4a4d4f,#6b6e70 55%,#3d4042);text-align:center;color:#fff}
.promo p{font-size:8.5px;line-height:13px;margin-top:29px}
.promo .vendor{font-size:15px;font-weight:700;margin-top:6px}
.promo .vendor i{display:inline-block;width:11px;height:11px;border-radius:50%;background:#8dc63f;margin-right:4px;vertical-align:-1px}
.promo .order{display:inline-block;margin-top:18px;background:#84c257;color:#fff;font-size:10px;font-weight:700;padding:6px 18px;border-radius:14px;letter-spacing:.3px}
.dates-title{left:18px;top:172px;color:var(--green);font-size:14px;font-weight:500}
.dates-title svg{vertical-align:-4px;margin-right:4px}
.dates-text{left:18px;top:199px;width:175px;font-size:9.5px;font-weight:500;line-height:15px;color:var(--ink-strong)}
.social-band{left:134px;top:442px;width:501px;height:57px;background:linear-gradient(105deg,#1f89bb 0%,#177db0 55%,#1e8fbf 100%);color:#fff}
.social-band .disc{left:29px;top:11px;width:36px;height:36px;border-radius:50%;background:#fff}
.social-band p{left:86px;top:14px;width:400px;font-size:12.5px;font-weight:700;line-height:17px}
.section-head{left:134px;top:520px;width:501px;height:33px;background:var(--panel);border-bottom:2px solid var(--green-soft);color:var(--green);font-size:14.5px;font-weight:500;padding:9px 18px}
.need-title{left:154px;top:561px;font-size:16px;font-weight:300;color:var(--ink)}
.facts{left:154px;top:590px;width:480px;list-style:none}
.facts li{font-size:10.5px;line-height:16.5px;color:var(--ink-soft);padding-left:17px;position:relative;margin-bottom:10px}
.facts li::before{content:"";position:absolute;left:0;top:5px;width:8px;height:8px;border-radius:50%;background:var(--dot)}
.services-lead{left:154px;top:679px;width:462px;font-size:12.8px;font-weight:700;color:var(--ink-strong);line-height:15.5px}
.service{font-size:10.5px;color:var(--ink-soft);line-height:14px;padding-left:16px;width:175px}
.service::before{content:"";position:absolute;left:0;top:4px;width:6px;height:6px;background:var(--dot)}
.info{left:156px;top:831px;width:443px;height:369px;background:var(--yellow)}
.info h2{left:0;width:443px;top:8px;text-align:center;color:#fff;font-size:26px;font-weight:900;text-shadow:0 0 2px #c9a800,1px 1px 0 #b89a00}
.info .intro{left:50px;width:343px;top:45px;text-align:center;font-size:6.4px;line-height:9px;color:#333}
.info .dash{left:13px;width:417px;top:76px;border-top:1px dashed #666}
.stat{width:70px;text-align:center;top:85px}
.stat .pic{width:62px;height:62px;border-radius:50%;background:#fff;margin:0 auto;border:2px solid #fff6a0;box-shadow:inset 0 0 0 14px #eeeeee}
.stat p{font-size:6.4px;line-height:9.3px;color:#444;margin-top:11px}
.card{background:#fff}
.map{left:10px;top:12px;width:100px;height:46px;background:var(--yellow);border-radius:6px 18px 8px 22px}
.card .note{left:118px;top:14px;width:88px;font-size:8.5px;font-weight:700;line-height:11.5px;color:#333}
.card h3{font-size:11px;font-weight:500;color:#333}
.card .def{font-size:7.8px;line-height:11.6px;color:#444}
.habit{width:40px;height:40px;border-radius:50%;background:#9a9a9a;top:28px}
</style>
</head>
<body>
<div class="abs view-online"><svg width="18" height="13" viewBox="0 0 18 13"><rect x="1" y="1" width="16" height="11" fill="none" stroke="#ef8450" stroke-width="1.4"/><path d="M1 1l8 6 8-6" fill="none" stroke="#ef8450" stroke-width="1.4"/></svg>View this email online</div>

<div class="abs sheet"></div>
<header class="abs masthead">
  <div class="abs brand"><span class="mark"></span><div><span class="name">The Bright Path</span><span class="sub">FAMILY MEDICINE</span></div></div>
</header>

<h2 class="abs issue-title">In This Issue:</h2>
<ul class="abs issue-list">
  <li>Comfort Outreach Month</li>
  <li>15 minutes of fame</li>
  <li>It's Official</li>
  <li>Don't Operate, Regenerate!</li>
  <li>Back to School Lumaderm Special</li>
  <li>Your Sinus Solution</li>
  <li>Breast Thermography</li>
  <li>Get Fit for Fall</li>
  <li>Recipe of the Month</li>
  <li>Feedback Wanted</li>
</ul>

<aside class="abs side-box">
  <div class="abs promo" role="img" aria-label="Supplement bottles on a pharmacy shelf">
    <p>Purchase professional-grade<br>supplements through</p>
    <div class="vendor"><i></i>Supplimo</div>
    <span class="order">PLACE ORDER</span>
  </div>
  <div class="abs dates-title"><svg width="20" height="20" viewBox="0 0 20 20"><circle cx="10" cy="11" r="7" fill="none" stroke="#6cb33f" stroke-width="2"/><path d="M10 7v4l3 2" fill="none" stroke="#6cb33f" stroke-width="2"/><path d="M2 5l3-3M18 5l-3-3" stroke="#6cb33f" stroke-width="2"/></svg>Upcoming Dates</div>
  <div class="abs dates-text">Get Fit For Fall Kickoff 9/18 Back to School Lumaderm Special&nbsp; 9/22-23rd</div>
</aside>

<div class="abs social-band">
  <div class="abs disc"></div>
  <p class="abs">Please like and follow us on Linkwall! We share regular updates and health tips</p>
</div>

<h2 class="abs section-head">September is Comfort Outreach Month</h2>
<h3 class="abs need-title">What You Need to Know</h3>
<ul class="abs facts">
  <li>Nearly 100 million Americans experience chronic pain —more than those who have diabetes, heart disease and cancer combined.</li>
  <li>Pain is a warning sign that indicates a problem that needs attention, don't just mask your symptoms, let us help try to get to the root of your issue.</li>
</ul>
<p class="abs services-lead">Check out some of the many services we have that can help you with your pain:</p>
<div class="abs service" style="left:154px;top:726px">Osteopathic Manipulation</div>
<div class="abs service" style="left:154px;top:750px">Acupuncture</div>
<div class="abs service" style="left:154px;top:776px">Prolotherapy, PRP, and Stem Cell Injections</div>
<div class="abs service" style="left:353px;top:726px">Spinal Decompression</div>
<div class="abs service" style="left:353px;top:750px">Infrared Sauna,</div>
<div class="abs service" style="left:353px;top:774px">Hyperbaric Oxygen,</div>

<section class="abs info">
  <h2 class="abs">National Comfort Outreach Month</h2>
  <p class="abs intro">National Comfort Outreach Month was created to increase awareness about the effects of pain, open the lines of communication in our local communities so that pain can be better understood and managed, and to educate citizens about the advanced treatment options available to help alleviate pain.</p>
  <div class="abs dash"></div>
  <div class="abs stat" style="left:7px"><div class="pic" role="img" aria-label="Figure with pain target on shoulder"></div><p>Pain affects more Americans than diabetes, heart disease and cancer combined.¹</p></div>
  <div class="abs stat" style="left:78px"><div class="pic" role="img" aria-label="Clock icon"></div><p>Workers lose an average of 4.6 hours per week of productive time due to a pain condition.²</p></div>
  <div class="abs stat" style="left:149px"><div class="pic" role="img" aria-label="Sleep cloud icon"></div><p>An estimated 20 percent of American adults report that pain or discomfort disrupts their sleep a few nights a week or more.³</p></div>
  <div class="abs stat" style="left:220px"><div class="pic" role="img" aria-label="Figure with back pain"></div><p>80 percent of people in the United States will experience back pain at some point in their lives.⁴</p></div>
  <div class="abs stat" style="left:291px"><div class="pic" role="img" aria-label="Tissue box icon"></div><p>Besides the common cold, back pain is the number one reason people visit their family doctors.⁵</p></div>
  <div class="abs stat" style="left:362px"><div class="pic" role="img" aria-label="Figure pushing shopping cart"></div><p>83 million Americans indicate that pain affects basic functioning in their everyday lives.⁶</p></div>

  <div class="abs card" style="left:13px;top:225px;width:204px;height:70px">
    <div class="abs map" role="img" aria-label="Map of the United States"></div>
    <p class="abs note">September is National Comfort Outreach Month across the United States.</p>
  </div>
  <div class="abs card" style="left:226px;top:225px;width:204px;height:112px;padding:6px 7px">
    <h3>What is Pain?</h3>
    <p class="def" style="margin-top:9px"><b>Oakridge Dictionary:</b> Physical suffering or discomfort caused by illness or injury.</p>
    <p class="def" style="margin-top:7px"><b>Dorwin Medical Dictionary:</b> A more or less localized sensation of discomfort, distress or agony resulting from the stimulation of specialized nerve endings.</p>
  </div>
  <div class="abs card" style="left:13px;top:305px;width:204px;height:64px;padding:6px 7px">
    <h3>Daily Habits to Help Reduce Pain:</h3>
    <div class="abs habit" style="left:5px" role="img" aria-label="Family icon"></div>
    <div class="abs habit" style="left:55px" role="img" aria-label="No smoking icon"></div>
    <div class="abs habit" style="left:105px" role="img" aria-label="Strawberry icon"></div>
    <div class="abs habit" style="left:155px" role="img" aria-label="Bicycle icon"></div>
  </div>
  <div class="abs card" style="left:226px;top:347px;width:204px;height:22px;padding:6px 10px">
    <h3>Goals of Comfort Outreach Month</h3>
  </div>
</section>
</body>
</html>
```